Morrow Interiors

Hi, can you please make this design up for me. Morrow interiors text to front and Beatrice Morrow text to back in black. Small love hearts to be black. Mobile number to front text and back mobile number and email address text to be white. Open to your input 🙂 Thanks in advance! Beatrice

Industry/Entity Type

Interior Design

Colors

Designer to choose only greyscale colors for use in the design.

Requirements
Must have
• Little love hearts for dot on i

```html
<!DOCTYPE html>
<html lang="en">
<head>
<meta charset="utf-8">
<title>Morrow Interiors – Business Cards</title>
<link rel="stylesheet" href="https://fonts.googleapis.com/css2?family=Bebas+Neue&family=Exo+2:wght@400&family=Roboto:wght@300&display=swap">
<style>
  :root {
    --backdrop: #262626;
    --backdrop-edge: #141414;
    --card-dark: #1f1f1f;
    --card-light: #ffffff;
    --ink-dark: #1e1e1e;
    --ink-light: #f2f2f2;
    --ink-muted: #d6d6d6;
    --rule: #8a8a8a;
  }
  * { margin: 0; padding: 0; box-sizing: border-box; }
  html, body { width: 1200px; height: 900px; overflow: hidden; }
  body {
    background: radial-gradient(ellipse at 55% 40%, var(--backdrop) 0%, var(--backdrop-edge) 100%);
    display: flex;
    align-items: center;
    justify-content: center;
    gap: 40px;
  }
  .card {
    width: 540px;
    height: 309px;
    position: relative;
    box-shadow: 0 18px 40px rgba(0,0,0,0.55);
  }
  .card--back { background: var(--card-dark); }
  .card--front { background: var(--card-light); }

  .card__name {
    position: absolute;
    left: 48px;
    top: 58px;
    font-family: "Bebas Neue", sans-serif;
    font-size: 40px;
    letter-spacing: 1.5px;
    color: var(--ink-light);
    line-height: 1;
  }
  .card__rule {
    position: absolute;
    left: 48px;
    top: 112px;
    width: 170px;
    height: 1px;
    background: linear-gradient(90deg, var(--rule), transparent);
  }
  .card__contact {
    position: absolute;
    left: 48px;
    top: 128px;
    font-family: "Roboto", sans-serif;
    font-weight: 300;
    font-size: 16px;
    line-height: 24px;
    color: var(--ink-muted);
    list-style: none;
  }

  .card__company {
    position: absolute;
    left: 0;
    right: 0;
    top: 110px;
    text-align: center;
    font-family: "Exo 2", sans-serif;
    font-weight: 400;
    font-size: 34px;
    letter-spacing: 1px;
    color: var(--ink-dark);
  }
  .card__mark {
    position: absolute;
    right: 52px;
    bottom: 44px;
    width: 62px;
    height: 62px;
    border-radius: 50%;
    background: var(--ink-dark);
  }
</style>
</head>
<body>
  <section class="card card--back">
    <h1 class="card__name">Beatrice Morrow</h1>
    <div class="card__rule"></div>
    <ul class="card__contact">
      <li>P : 321 5550-1742</li>
      <li>E : info@BeatriceMorrow.com</li>
    </ul>
  </section>

  <section class="card card--front">
    <h2 class="card__company">Morrow Interiors</h2>
    <div class="card__mark"></div>
  </section>
</body>
</html>
```